Pat Greene Billboard

**Task Description: Billboard Design for Self Storage Facility**

**Objective:**
Design a captivating billboard to promote our self-storage facility with a focus on our convenient location and online rental capabilities.

**Key Messages to Include:**
1. **Location Emphasis:** Highlight that our facility is located right beside the billboard (maybe by using an arrow pointing left).
2. **Online Rental Convenience:** Feature prominently that customers can "Rent Online Anytime!” or that we are "Always Open Online!"

**Target Audience:**
- Local residents looking for convenient self-storage solutions.
- Businesses needing storage space accessible around the clock.

**Design Elements:**
1. **Visual Impact:** Eye-catching graphics and colors that stand out against the surroundings.
2. **Clear Text:** Bold and concise messaging that can be read and understood quickly.
3. **Contact Information:** Include our phone number and website URL for easy access to further information.

**Additional Information:**
- Billboard dimensions: 12 ft. x 24 ft.
- Preferred color scheme: Bright and attention-grabbing, but professional.
- Branding: Incorporate our logo and brand colors to maintain consistency.

**Deliverables:**
- High-resolution digital file compatible with billboard printing specifications.
- Consider mockups or visualizations for presentation purposes.

Please note that I have attached current logos/graphics that we would love to incorporate into the billboard as well as a picture of our current billboard. Our logo (Pat Greene Self Storage - PG navy.png) MUST be incorporated into the billboard. Also feel free to add any of the current descriptions from the picture of our current billboard into the design. Instead of using "Climate Controlled" use "Temperature Controlled". Thank you for your attention to these details. We look forward to reviewing your proposed design!

```html
<!DOCTYPE html>
<html lang="en">
<head>
<meta charset="utf-8">
<title>Pat Greene Billboard</title>
<link href="https://fonts.googleapis.com/css2?family=Bebas+Neue&family=Montserrat:wght@600;700&display=swap" rel="stylesheet">
<style>
  :root {
    --navy: #0f2a5c;
    --brown: #8b6b4d;
    --slate: #3f5679;
    --white: #ffffff;
    --page: #c9c9c9;
    --photo-light: #d9dbde;
    --photo-mid: #a9adb2;
    --photo-floor: #b7aa97;
  }
  html, body {
    margin: 0;
    padding: 0;
    width: 933px;
    height: 1200px;
    overflow: hidden;
    background: var(--page);
  }
  .canvas {
    position: relative;
    width: 933px;
    height: 1200px;
  }
  .billboard {
    position: absolute;
    left: 0;
    top: 0;
    width: 1080px;
    height: 571px;
    transform: translate(61.5px, 386px) scale(0.75);
    transform-origin: 0 0;
    box-shadow: 0 6px 14px rgba(0,0,0,0.35);
    overflow: hidden;
    font-family: "Bebas Neue", "Oswald", sans-serif;
    color: var(--white);
  }
  .billboard__shapes {
    position: absolute;
    inset: 0;
  }
  .brand {
    position: absolute;
    left: 548px;
    top: 0;
    width: 355px;
    height: 95px;
    background: var(--white);
    border-radius: 0 0 14px 14px;
    display: flex;
    align-items: center;
    justify-content: center;
    gap: 10px;
  }
  .brand__dot {
    flex: none;
    width: 14px;
    height: 14px;
    border-radius: 50%;
    background: var(--brown);
  }
  .brand__name {
    font-family: "Bebas Neue", sans-serif;
    font-size: 34px;
    color: var(--navy);
    letter-spacing: 1px;
    line-height: 1;
    white-space: nowrap;
    padding-top: 4px;
  }
  .headline {
    position: absolute;
    left: 460px;
    width: 572px;
    top: 110px;
    margin: 0;
    text-align: center;
    font-weight: 400;
    font-size: 68px;
    line-height: 56px;
  }
  .tagline {
    position: absolute;
    left: 500px;
    top: 231px;
    width: 490px;
    height: 25px;
    margin: 0;
    background: var(--brown);
    border-radius: 4px;
    font-family: "Montserrat", sans-serif;
    font-weight: 700;
    font-size: 14px;
    line-height: 25px;
    text-align: center;
  }
  .why {
    position: absolute;
    left: 460px;
    width: 572px;
    top: 274px;
    margin: 0;
    text-align: center;
    font-weight: 400;
    font-size: 44px;
    line-height: 44px;
  }
  .features {
    position: absolute;
    left: 494px;
    top: 338px;
    width: 536px;
    height: 76px;
    display: flex;
    margin: 0;
    padding: 0;
    list-style: none;
  }
  .feature {
    flex: 1;
    display: flex;
    flex-direction: column;
    align-items: center;
    font-family: "Montserrat", sans-serif;
    font-weight: 700;
    font-size: 11.5px;
    line-height: 12px;
    text-align: center;
    padding-top: 10px;
  }
  .feature + .feature {
    border-left: 2px solid var(--white);
  }
  .feature svg {
    width: 26px;
    height: 24px;
    margin-bottom: 6px;
  }
  .rent {
    position: absolute;
    left: 488px;
    top: 468px;
    width: 200px;
    display: flex;
    align-items: center;
    gap: 10px;
  }
  .rent svg {
    flex: none;
    width: 56px;
    height: 44px;
  }
  .rent__text {
    font-size: 31px;
    line-height: 31px;
  }
  .contact {
    position: absolute;
    left: 690px;
    right: 0;
    top: 458px;
    text-align: center;
    font-size: 51px;
    line-height: 50px;
  }
</style>
</head>
<body>
<div class="canvas">
  <section class="billboard">
    <svg class="billboard__shapes" viewBox="0 0 1080 571" width="1080" height="571">
      <defs>
        <linearGradient id="photoTone" x1="0" y1="0" x2="0.6" y2="1">
          <stop offset="0" stop-color="var(--photo-light)"/>
          <stop offset="0.55" stop-color="var(--photo-mid)"/>
          <stop offset="1" stop-color="var(--photo-floor)"/>
        </linearGradient>
      </defs>
      <rect role="img" aria-label="Photo of a storage unit hallway with roll-up doors and a blue platform cart" x="0" y="0" width="560" height="571" fill="url(#photoTone)"/>
      <polygon points="290,0 1080,0 1080,571 470,571" fill="var(--brown)"/>
      <polygon points="301,0 1080,0 1080,444 475,444" fill="var(--navy)"/>
      <polygon points="470,444 1080,444 1080,571 470,571" fill="var(--brown)"/>
      <polygon points="272,571 410,410 470,571" fill="var(--slate)"/>
    </svg>

    <div class="brand">
      <span class="brand__dot"></span>
      <span class="brand__name">Pat Greene Self Storage</span>
    </div>

    <h1 class="headline">Self Storage in<br>The Heart of Georgia</h1>
    <p class="tagline">Elevate your storage experience with Summit Storage Group</p>
    <h2 class="why">Why Choose Summit Storage Group?</h2>

    <ul class="features">
      <li class="feature">
        <svg viewBox="0 0 26 24" fill="none" stroke="var(--white)" stroke-width="1.5" stroke-linejoin="round" stroke-linecap="round">
          <path d="M1 9l5-4 4 2 4-2 5 0 6 4"/>
          <path d="M4 12l7 7c1 1 2 1 3 0l7-7"/>
          <path d="M10 8l-3 3c-1 1 0 2 1 2l4-3"/>
        </svg>
        NO Long-Term<br>Commitments
      </li>
      <li class="feature">
        <svg viewBox="0 0 26 24" fill="none" stroke="var(--white)" stroke-width="1.5">
          <path d="M13 22s-7-7-7-12a7 7 0 0 1 14 0c0 5-7 12-7 12z"/>
          <circle cx="13" cy="10" r="2.5"/>
        </svg>
        Locally Owned<br>&amp; Managed
      </li>
      <li class="feature">
        <svg viewBox="0 0 26 24" fill="none" stroke="var(--white)" stroke-width="1.5" stroke-linecap="round">
          <path d="M11 4a2 2 0 0 1 4 0v10a4 4 0 1 1-4 0z"/>
          <circle cx="13" cy="17.5" r="1.5"/>
        </svg>
        Temperature<br>Controlled
      </li>
      <li class="feature">
        <svg viewBox="0 0 26 24" fill="none" stroke="var(--white)" stroke-width="1.5" stroke-linecap="round" stroke-linejoin="round">
          <path d="M20 12a8 8 0 1 1-4-7"/>
          <path d="M8 11l4 4 11-11"/>
        </svg>
        A Variety of<br>Storage Options
      </li>
    </ul>

    <div class="rent">
      <svg viewBox="0 0 56 44" fill="var(--white)" aria-label="Arrow pointing left to the facility" role="img">
        <polygon points="0,22 24,0 24,13 56,13 56,31 24,31 24,44"/>
      </svg>
      <div class="rent__text">Rent Online<br>Anytime!</div>
    </div>

    <div class="contact">(478) 555-0142<br>www.patgreene.com</div>
  </section>
</div>
</body>
</html>
```